BIX Promotional flyer for students

We're looking for an 8.5" x 11" flyer that will be distributed to schools. Please see language to include in attached files.

Target Market(s)

The parents and teachers of high school students

Industry/Entity Type

Mental health

Other font styles liked:
• Monserrat and Roboto Slab

Requirements
Must have
• See attached pdf for language to be included on the flyer. Please use the color palette from our website: www.bixzone.tv. Please include some imagery of students. Please ensure the
Nice to have
• Feel free to use any of the graphics provided. See our website for our brand look & feel: www.bixzone.tv

```html
<!DOCTYPE html>
<html lang="en">
<head>
<meta charset="utf-8">
<title>Fundraise with BIX – Flyer</title>
<link rel="stylesheet" href="https://fonts.googleapis.com/css2?family=Montserrat:wght@300;400;500;700;800&display=swap">
<style>
  :root {
    --teal: #70aeb4;
    --orange: #ee7d38;
    --ink: #111111;
    --paper: #ffffff;
    --backdrop: #c8c8c8;
  }
  * { margin: 0; padding: 0; box-sizing: border-box; }
  html, body {
    width: 1200px; height: 1200px; overflow: hidden;
    background: var(--backdrop);
    font-family: "Montserrat", Arial, sans-serif;
  }
  .flyer {
    position: absolute; left: 182px; top: 57px;
    width: 835px; height: 1080px;
    background: var(--paper);
    box-shadow: 2px 3px 6px rgba(0,0,0,.25);
    overflow: hidden;
  }
  .flyer-shapes { position: absolute; inset: 0; }
  .headline {
    position: absolute; left: 52px; top: 50px;
    color: var(--paper); font-size: 60px; line-height: 73px;
    text-transform: uppercase; letter-spacing: 1px;
  }
  .headline .light { font-weight: 300; display: block; }
  .headline .bold { font-weight: 800; display: block; }
  .brand {
    position: absolute; left: 660px; top: 58px;
    display: flex; align-items: center; gap: 10px;
  }
  .brand-dot { width: 40px; height: 40px; border-radius: 50%; background: var(--orange); }
  .brand-name { font-weight: 800; font-size: 52px; color: var(--orange); line-height: 1; }
  .proceeds {
    position: absolute; left: 52px; top: 340px;
    font-size: 35px; font-weight: 300; line-height: 41px;
    color: var(--ink); text-transform: uppercase;
  }
  .proceeds .figure { font-size: 56px; font-weight: 800; color: var(--teal); margin-right: 8px; }
  .rule {
    position: absolute; height: 3px; background: var(--orange);
  }
  .rule-mid { left: 53px; top: 545px; width: 140px; }
  .rule-foot { left: 732px; top: 947px; width: 103px; }
  .support {
    position: absolute; left: 52px; top: 582px;
    font-size: 35px; font-weight: 800; line-height: 41px;
    color: var(--orange); text-transform: uppercase;
  }
  .body-copy {
    position: absolute; left: 52px; top: 738px; width: 600px;
    font-size: 19px; font-weight: 400; line-height: 24.8px; color: var(--ink);
  }
  .site {
    position: absolute; left: 550px; top: 966px;
    font-size: 32px; font-weight: 800; color: var(--teal); letter-spacing: .5px;
  }
</style>
</head>
<body>
<main class="flyer">
  <svg class="flyer-shapes" width="835" height="1080" viewBox="0 0 835 1080">
    <defs>
      <linearGradient id="student-photo" x1="0" y1="0" x2="1" y2="1">
        <stop offset="0" stop-color="#8a5a45"/>
        <stop offset=".5" stop-color="#c9a48e"/>
        <stop offset="1" stop-color="#5f7b98"/>
      </linearGradient>
      <linearGradient id="tablet-photo" x1="0" y1="0" x2="0" y2="1">
        <stop offset="0" stop-color="#e4e1de"/>
        <stop offset=".6" stop-color="#cfc9c3"/>
        <stop offset="1" stop-color="#5b3a8e"/>
      </linearGradient>
    </defs>
    <path class="band-top" fill="var(--teal)" d="M0,0 H555 C520,130 440,245 300,290 C200,322 90,310 0,267 Z"/>
    <path class="band-bottom" fill="var(--teal)" d="M0,900 C120,935 245,1005 315,1080 H0 Z"/>
    <circle cx="562" cy="363" r="224" fill="var(--paper)"/>
    <circle cx="562" cy="363" r="221" fill="url(#student-photo)" role="img" aria-label="Photo of a smiling student in a grey beanie and denim jacket"/>
    <circle cx="649" cy="592" r="141" fill="var(--paper)"/>
    <circle cx="649" cy="592" r="137" fill="url(#tablet-photo)" role="img" aria-label="Photo of a student on a sofa writing on a tablet"/>
  </svg>

  <h1 class="headline"><span class="light">Fundraise</span><span class="bold">With BIX</span></h1>

  <div class="brand"><span class="brand-dot"></span><span class="brand-name">bix</span></div>

  <p class="proceeds"><span class="figure">50%</span>of all<br>proceeds<br>go back to<br>your school</p>

  <div class="rule rule-mid"></div>

  <h2 class="support">Support the<br>mental health<br>of your students</h2>

  <p class="body-copy">BIX is a simple and effective way to improve mental health. Your students will learn valuable coping skills and techniques from expert clinicians who analyze real cases and share their insights and advice.</p>

  <div class="rule rule-foot"></div>
  <p class="site">BIXZONE.TV</p>
</main>
</body>
</html>
```